innovative investment real estate sales firm

We are a uniquely collabrative firm that seeks to bring a conultative approach to uncovering hidden opportunities for our clients, our website needs to convey our client focused approach. Our firm specializes in the sale of apartment properties in Southern California. We have a team of researchers, transaction coordinators and marketing personal to support our geographically specialized advisers. We need a website that introduces clients to our unique way of better helping them achieve their investment goals.

Target Market(s)

High net worth individuals and families

Industry/Entity Type

Real Estate Agent

Font styles to use
Other font styles liked:
• please use font provided

Requirements
Must have
• Stories of our recent projects
• Features on our people
• email capture for viewing inventory
• content that showcases our unique consultative approach that uncovers unrealized opportunities

```html
<!DOCTYPE html>
<html lang="en">
<head>
<meta charset="utf-8">
<title>Meridian Crest Advisors — Multifamily Investment Sales</title>
<link href="https://fonts.googleapis.com/css2?family=Open+Sans:wght@400;600;700;800&display=swap" rel="stylesheet">
<style>
:root{
  --green:#8dc63f;
  --green-dark:#76ad2c;
  --teal:#1a9fb0;
  --ink:#2b2b2b;
  --body:#6d6d6d;
  --slate:#3b4852;
  --night:#1f1f1f;
  --footer:#22201d;
  --line:#e3e3e3;
  --white:#ffffff;
}
*{box-sizing:border-box;margin:0;padding:0}
html,body{width:1200px;height:4082px;overflow:hidden}
body{font-family:"Open Sans",Arial,sans-serif;color:var(--body);background:var(--white);position:relative}
a{color:inherit;text-decoration:none}
.btn{display:inline-block;background:var(--teal);color:var(--white);font-size:11px;font-weight:700;letter-spacing:.5px;text-transform:uppercase;padding:10px 22px;border-radius:20px}
.section-title{text-align:center;font-size:24px;font-weight:700;color:var(--ink)}
.section-title span{color:var(--green)}
.ph{position:absolute}

/* header */
.site-header{position:absolute;left:0;top:0;width:1200px;height:90px;background:var(--white);display:flex;align-items:center;justify-content:space-between;padding:0 90px 0 110px}
.brand{display:flex;align-items:center;gap:12px;font-weight:800;font-size:20px;color:var(--slate);letter-spacing:1px}
.brand .mark{width:34px;height:34px;background:var(--slate)}
.main-nav{display:flex;gap:26px;font-size:11px;font-weight:700;color:var(--ink)}

/* hero */
.hero{position:absolute;left:0;top:90px;width:1200px;height:595px;background:linear-gradient(180deg,#2a2f2b 0%,#3b3f35 45%,#1e3238 75%,#12262c 100%)}
.hero-card{position:absolute;left:114px;top:180px;width:376px;height:210px;background:rgba(141,198,63,.9);padding:22px 24px;color:var(--white)}
.hero-card h1{font-size:22px;font-weight:800;margin-bottom:10px}
.hero-card p{font-size:11px;line-height:1.5;margin-bottom:18px}
.hero-card .btn{background:var(--white);color:var(--green-dark);border-radius:0;padding:9px 16px}
.hero-arrow{position:absolute;top:270px;width:24px;height:30px}

/* property description */
.property{position:absolute;left:0;top:685px;width:1200px;height:673px}
.property .section-title{margin-top:60px}
.property .lead{width:900px;margin:26px auto 0;text-align:center;font-size:12px;line-height:1.7}
.feature{position:absolute;width:220px;height:220px;border-radius:50%;background:var(--green);border:8px solid var(--white);box-shadow:0 0 0 2px var(--green);display:flex;flex-direction:column;align-items:center;justify-content:center;color:var(--white);font-weight:700;font-size:14px;gap:6px}
.property .btn{position:absolute;left:538px;top:575px}

/* about */
.about{position:absolute;left:0;top:1358px;width:1200px;height:335px;display:flex}
.about-photo{width:522px;height:335px;background:linear-gradient(135deg,#cfc6b8,#8a7a68 60%,#5e5046)}
.about-body{flex:1;background:var(--slate);color:#d7dde1;padding:38px 60px 0 38px}
.about-body h2{color:var(--white);font-size:22px;margin-bottom:14px}
.about-body h2 span{color:var(--green)}
.about-body p{font-size:11.5px;line-height:1.7;margin-bottom:22px}

/* gallery */
.gallery{position:absolute;left:0;top:1693px;width:1200px;height:960px}
.gallery .section-title{margin-top:70px}
.tile{position:absolute}
.gallery .btn{position:absolute;left:545px;top:870px}

/* team */
.team{position:absolute;left:0;top:2640px;width:1200px;height:460px}
.team .section-title{margin-top:18px}
.team-intro{position:absolute;left:114px;top:112px;width:310px;font-size:11.5px;line-height:1.7}
.roles{position:absolute;left:114px;top:245px;list-style:none;font-size:13px;color:var(--ink)}
.roles li{display:flex;align-items:center;gap:12px;margin-bottom:20px}
.roles .tick{width:16px;height:16px;border-radius:50%;background:var(--teal);display:flex;align-items:center;justify-content:center}
.member{position:absolute;background:linear-gradient(180deg,#e9e6e1,#bcb4aa)}
.member .tag{position:absolute;left:0;bottom:0;width:100%;padding:10px 14px;color:var(--white);font-size:12px;font-weight:700;background:rgba(59,72,82,.85)}
.member .tag small{display:block;font-size:10px;font-weight:400;opacity:.8}
.member.featured .tag{background:var(--slate)}

/* testimonial */
.testimonial{position:absolute;left:0;top:3100px;width:1200px;height:254px;background:var(--night);color:#c9c9c9;padding:62px 0 0 220px}
.testimonial .quote{position:absolute;left:190px;top:58px;font-size:34px;color:var(--white);font-weight:800;line-height:1}
.testimonial p{width:780px;font-size:11.5px;line-height:1.7}
.client{display:flex;align-items:center;gap:12px;margin-top:24px;margin-left:40px}
.client .avatar{width:34px;height:34px;border-radius:50%;background:var(--teal)}
.client b{display:block;color:var(--white);font-size:12px}
.client small{font-size:10px}

/* subscribe */
.subscribe{position:absolute;left:0;top:3354px;width:1200px;height:338px;text-align:center}
.subscribe .section-title{margin-top:58px}
.subscribe p{width:760px;margin:24px auto 0;font-size:11.5px;line-height:1.7}
.signup{display:flex;justify-content:center;margin-top:34px}
.signup .field{width:330px;height:36px;border:1px solid #cfcfcf;font-size:11px;text-align:left;padding:10px 14px;color:#9a9a9a}
.signup .go{height:36px;background:var(--teal);color:var(--white);font-size:11px;font-weight:700;padding:11px 22px}

/* footer */
.site-footer{position:absolute;left:0;top:3692px;width:1200px;height:390px;background:linear-gradient(180deg,#2e2a26,#1c1a18);color:#bdb6ad}
.footer-col{position:absolute;top:42px;font-size:11.5px;line-height:1.8}
.footer-col h3{color:var(--white);font-size:14px;font-weight:700;margin-bottom:14px;letter-spacing:.5px}
.footer-col ul{list-style:none}
.footer-col li::before{content:"› ";color:var(--green)}
.contact-line{display:flex;gap:10px;align-items:flex-start;margin-bottom:10px}
.contact-line .ico{width:22px;height:22px;border-radius:50%;background:var(--teal);flex:none;display:flex;align-items:center;justify-content:center}
.social{position:absolute;left:0;width:1200px;top:320px;display:flex;justify-content:center;gap:10px}
.social i{width:12px;height:12px;border-radius:50%;background:#6f6a63;display:block}
.copyright{position:absolute;left:0;width:1200px;top:345px;text-align:center;font-size:10.5px}
</style>
</head>
<body>

<header class="site-header">
  <a class="brand" href="#"><span class="mark"></span>MERIDIAN CREST ADVISORS</a>
  <nav class="main-nav">
    <a href="#">HOME</a><a href="#">ABOUT US</a><a href="#">PROPERTIES</a><a href="#">RECENT PROJECTS</a><a href="#">OUR AGENTS</a><a href="#">CONTACT</a>
  </nav>
</header>

<section class="hero" role="img" aria-label="Evening view of a luxury apartment courtyard with palm trees and a lit pool">
  <svg class="hero-arrow" style="left:40px" viewBox="0 0 24 30"><path d="M16 4 6 15l10 11" fill="none" stroke="#fff" stroke-width="3"/></svg>
  <svg class="hero-arrow" style="right:40px" viewBox="0 0 24 30"><path d="M8 4l10 11L8 26" fill="none" stroke="#fff" stroke-width="3"/></svg>
  <div class="hero-card">
    <h1>MULTIFAMILY PROPERTIES</h1>
    <p>We uncover hidden value in Southern California apartment assets, guiding each client with research, careful planning and local insight so every sale meets long term investment goals.</p>
    <a class="btn" href="#">EXPLORE MORE</a>
  </div>
</section>

<section class="property">
  <h2 class="section-title">Property <span>Description</span></h2>
  <p class="lead">Every listing we bring to market is studied from the ground up. Our researchers review rents, unit mix, zoning and upside so that owners and buyers see the full picture. This consultative approach reveals opportunities others miss and helps our clients act with confidence in a changing market.</p>
  <div class="feature" style="left:380px;top:190px">
    <svg width="46" height="30" viewBox="0 0 46 30"><path d="M3 4v24M3 20h40v8M3 14h12v6M17 12h22a4 4 0 0 1 4 4v4H17z" fill="none" stroke="#fff" stroke-width="3"/></svg>Bedrooms</div>
  <div class="feature" style="left:604px;top:190px">
    <svg width="44" height="34" viewBox="0 0 44 34"><path d="M4 16h36v4a10 10 0 0 1-10 10H14A10 10 0 0 1 4 20zM10 16V6a4 4 0 0 1 8 0M12 30l-2 4M32 30l2 4" fill="none" stroke="#fff" stroke-width="3"/></svg>Bathrooms</div>
  <div class="feature" style="left:492px;top:360px">
    <svg width="36" height="36" viewBox="0 0 36 36"><rect x="3" y="6" width="30" height="27" fill="none" stroke="#fff" stroke-width="3"/><path d="M3 14h30M10 2v8M26 2v8" stroke="#fff" stroke-width="3"/></svg>Built Year</div>
  <a class="btn" href="#">VIEW ALL FEATURES</a>
</section>

<section class="about">
  <div class="about-photo" role="img" aria-label="Bright modern living room with sofas and tall windows"></div>
  <div class="about-body">
    <h2>About <span>Us</span></h2>
    <p>We are a collaborative firm that brings a consultative approach to apartment investment sales. Our advisers focus on specific neighborhoods, backed by a team of researchers, transaction coordinators and marketing staff. Together we study each property in depth, share clear guidance and help owners and families plan their next move with care. Clients stay at the center of every decision, from first review to final closing.</p>
    <a class="btn" href="#">LEARN MORE</a>
  </div>
</section>

<section class="gallery">
  <h2 class="section-title">Project <span>Gallery</span></h2>
  <div class="tile" role="img" aria-label="Modern kitchen interior" style="left:114px;top:151px;width:314px;height:200px;background:linear-gradient(135deg,#e8e8e6,#b9bcbc)"></div>
  <div class="tile" role="img" aria-label="Bright living area with large windows" style="left:114px;top:361px;width:314px;height:200px;background:linear-gradient(135deg,#d9dcd8,#8f9a8f)"></div>
  <div class="tile" role="img" aria-label="Open lounge with warm lighting and fireplace" style="left:441px;top:151px;width:644px;height:410px;background:linear-gradient(160deg,#6d5a46,#3a3028 55%,#1f2a33)"></div>
  <div class="tile" role="img" aria-label="Living room with green sofa" style="left:114px;top:571px;width:314px;height:200px;background:linear-gradient(135deg,#e9e7e2,#7f8a6c)"></div>
  <div class="tile" role="img" aria-label="Minimal furnished interior" style="left:441px;top:571px;width:316px;height:200px;background:linear-gradient(135deg,#efece6,#c4b9a8)"></div>
  <div class="tile" role="img" aria-label="Apartment living space with tall windows" style="left:769px;top:571px;width:316px;height:200px;background:linear-gradient(135deg,#dcdad5,#9c9283)"></div>
  <a class="btn" href="#">VIEW MORE</a>
</section>

<section class="team">
  <h2 class="section-title">Meet Our <span>Team</span></h2>
  <p class="team-intro">Our geographically focused advisers are supported by specialists who handle research, deal flow and marketing. Each team member brings local knowledge and a shared commitment to clear, honest advice for every client.</p>
  <ul class="roles">
    <li><span class="tick"><svg width="9" height="8" viewBox="0 0 9 8"><path d="M1 4l2.5 2.5L8 1" fill="none" stroke="#fff" stroke-width="1.8"/></svg></span>Researcher</li>
    <li><span class="tick"><svg width="9" height="8" viewBox="0 0 9 8"><path d="M1 4l2.5 2.5L8 1" fill="none" stroke="#fff" stroke-width="1.8"/></svg></span>Transaction coordination</li>
    <li><span class="tick"><svg width="9" height="8" viewBox="0 0 9 8"><path d="M1 4l2.5 2.5L8 1" fill="none" stroke="#fff" stroke-width="1.8"/></svg></span>Marketing Executive</li>
  </ul>
  <div class="member" role="img" aria-label="Portrait of team researcher" style="left:441px;top:155px;width:212px;height:245px"><div class="tag">Miss. Example Name<small>Researcher</small></div></div>
  <div class="member featured" role="img" aria-label="Portrait of senior adviser" style="left:661px;top:102px;width:216px;height:298px"><div class="tag">Mr. Example Name<small>Senior Adviser</small></div></div>
  <div class="member" role="img" aria-label="Portrait of marketing executive" style="left:877px;top:155px;width:208px;height:245px"><div class="tag">Miss. Example Name<small>Marketing</small></div></div>
</section>

<section class="testimonial">
  <span class="quote">“</span>
  <p>Working with this team changed how we look at our properties. They took time to learn our goals, found value we had not seen and guided us through each step of the sale with patience and skill. We felt informed and supported from start to finish.</p>
  <div class="client"><span class="avatar"></span><div><b>CLIENT NAME</b><small>Property Owner, Orange County</small></div></div>
</section>

<section class="subscribe">
  <h2 class="section-title">Subscribe &amp; <span>Be Up-to-Date</span></h2>
  <p>Join our list to view current inventory, new listings and market notes from our advisers. We share only what helps you make better investment decisions.</p>
  <div class="signup"><span class="field">Enter your Email</span><span class="go">SUBSCRIBE</span></div>
</section>

<footer class="site-footer" role="img" aria-label="Dusk view of apartment buildings behind footer content">
  <div class="footer-col" style="left:114px;width:300px">
    <h3>ABOUT US</h3>
    <p>We are a collaborative investment sales firm focused on apartment properties across Southern California, helping high net worth clients reach their goals.</p>
  </div>
  <div class="footer-col" style="left:441px;width:220px">
    <h3>QUICK MENU</h3>
    <ul><li>Home</li><li>About Us</li><li>Services &amp; Solutions</li><li>Testimonials &amp; Case Studies</li><li>News &amp; Events</li><li>Contact</li></ul>
  </div>
  <div class="footer-col" style="left:720px;width:340px">
    <h3>CONTACT US</h3>
    <div class="contact-line"><span class="ico"><svg width="11" height="11" viewBox="0 0 12 12"><path d="M2 1l3 2-1 2 3 3 2-1 2 3-2 1C5 11 1 7 1 3z" fill="#fff"/></svg></span><span>(555) 014-2278, (555) 016-9043</span></div>
    <div class="contact-line"><span class="ico"><svg width="11" height="9" viewBox="0 0 12 9"><rect x="1" y="1" width="10" height="7" fill="none" stroke="#fff"/><path d="M1 1l5 4 5-4" fill="none" stroke="#fff"/></svg></span><span>hello@meridiancrest.example<br>listings@meridiancrest.example</span></div>
    <div class="contact-line"><span class="ico"><svg width="9" height="12" viewBox="0 0 9 12"><path d="M4.5 11S1 7 1 4.5a3.5 3.5 0 0 1 7 0C8 7 4.5 11 4.5 11z" fill="#fff"/></svg></span><span>240 Harbor Vista Blvd, Suite 300,<br>Irvine, CA</span></div>
  </div>
  <div class="social"><i></i><i></i><i></i><i></i></div>
  <p class="copyright">Copyright © All Rights Reserved 2017</p>
</footer>

</body>
</html>
```